Consulting services and software brochure

We need a brochure designed that would ideally work with our logo and highlight a few of our consulting services and a couple products we offer. Our industry is real estate technology and we focus on consulting services for third party software systems. We would like the design to work well with our logo colors although we are open to changing either the blue or the orange to white in a design. The final design should clearly highlight our service options in an easy to read way while also leaving plenty of room to insert a lot of text on each service

What we like about our current design: it incorporates our colors well and has lots of room for text on each service, the two product offerings, and a couple testimonials from our clients

What we don’t like: It’s very busy and doesn’t highlight our offerings without a lot of reading. We also think it could have better layout, be much more polished and interesting visually (this was not designed by a professional).

Please provide source file compatible with Photoshop.

We are impressed with the designs so far and have made the payment guaranteed for this project. We will be starting to provide feedback early next week as we review internally.

Regarding size: We are open to a multi-page brochure or an 8 1/2 x 11, square shape, etc. After reviewing the designs we have decided the tri-folds seem to look too busy though on a standard piece of paper. Also, there's a good chance whatever designer we choose we will also hire to do another option in a different size/length so please don't worry either way too much about that.

Thanks for the great submissions so far!

Reason: Hi - we're extending the deadline a week since a few people providing input have been out this week for Passover and Good Friday. Thank you for your understanding.

Reason: Hi - we've settled on a designer and are now refining the brochure. Thank you everyone for your time and effort.

```html
<!DOCTYPE html>
<html lang="en">
<head>
<meta charset="utf-8">
<title>Northvale inc. – Consulting Services Brochure</title>
<link href="https://fonts.googleapis.com/css2?family=Cinzel:wght@400;600&family=Open+Sans:wght@400;600&display=swap" rel="stylesheet">
<style>
  :root {
    --backdrop: #e6e3de;
    --charcoal: #2e2e30;
    --cover-dark: #434345;
    --cover-band: #58585a;
    --white: #ffffff;
    --ink: #3a3a3a;
    --orange: #d4703c;
    --orange-soft: #dc8c52;
    --cyan: #27b5cf;
    --serif: "Cinzel", serif;
    --sans: "Open Sans", sans-serif;
  }
  * { box-sizing: border-box; margin: 0; padding: 0; }
  html, body { width: 1200px; height: 900px; overflow: hidden; }
  body { background: var(--backdrop); position: relative; font-family: var(--sans); }

  .page { position: absolute; top: 195px; width: 360px; height: 510px; overflow: hidden; }
  .cover { left: 40px; background: var(--cover-dark); box-shadow: 0 6px 18px rgba(0,0,0,.18); }
  .spread { position: absolute; left: 440px; top: 195px; width: 720px; height: 510px; box-shadow: 0 6px 18px rgba(0,0,0,.18); }
  .spread .page { top: 0; background: var(--charcoal); }
  .page-left { left: 0; }
  .page-right { left: 360px; border-left: 1px solid #1f1f20; }

  /* cover */
  .cover-head { position: absolute; left: 0; top: 0; width: 100%; height: 66px; background: var(--white); }
  .brand { position: absolute; right: 22px; top: 18px; display: flex; align-items: center; gap: 6px; }
  .brand-mark { width: 14px; height: 14px; background: var(--orange); }
  .brand-name { font-family: var(--sans); font-weight: 600; font-size: 17px; color: var(--ink); }
  .brand-tagline { position: absolute; right: 22px; top: 40px; font-size: 6.5px; letter-spacing: .8px; color: var(--ink); }
  .cover-rule { position: absolute; left: 0; top: 66px; width: 100%; height: 4px; background: var(--orange); }
  .cover-photo { position: absolute; left: 0; top: 70px; width: 100%; height: 262px;
    background: linear-gradient(135deg, #f2ece2 0%, #d9c6aa 45%, #b9a48a 75%, #e7e1d6 100%); }
  .cover-band { position: absolute; left: 0; top: 388px; width: 100%; height: 34px; background: var(--cover-band);
    display: flex; align-items: center; justify-content: center; }
  .cover-url { color: var(--white); font-size: 9px; letter-spacing: .5px; }

  /* left inner page */
  .intro-panel { position: absolute; left: 22px; top: 34px; width: 152px; height: 222px; background: var(--orange-soft); padding: 14px 12px; color: var(--white); }
  .intro-title { font-family: var(--serif); font-size: 13px; margin-bottom: 8px; }
  .intro-text { font-size: 9.5px; line-height: 1.55; }
  .photo-building { position: absolute; left: 182px; top: 24px; width: 156px; height: 232px;
    background: linear-gradient(160deg, #f4f4f2 0%, #c9d3d8 50%, #6d8aa0 100%); }
  .photo-family { position: absolute; left: 22px; top: 266px; width: 152px; height: 222px;
    background: linear-gradient(180deg, #cfe6f2 0%, #f4f7f8 55%, #d9694a 80%, #6f9a4f 100%); }
  .ask-panel { position: absolute; left: 182px; top: 266px; width: 156px; height: 200px; background: var(--cyan); padding: 12px 11px; color: var(--white); }
  .ask-title { font-family: var(--serif); font-size: 14px; margin-bottom: 8px; }
  .ask-list { list-style: none; font-size: 8.6px; line-height: 1.4; }
  .ask-list li { position: relative; padding-left: 8px; margin-bottom: 3px; }
  .ask-list li::before { content: "-"; position: absolute; left: 0; }

  /* services page */
  .services-title { position: absolute; left: 30px; top: 28px; font-family: var(--serif); font-size: 22px; letter-spacing: 1.5px; color: var(--white); }
  .services { position: absolute; left: 24px; top: 76px; width: 312px; }
  .service-row { display: flex; gap: 8px; height: 40px; margin-bottom: 9px; }
  .service-row.tall { height: 46px; }
  .service-number { width: 72px; background: var(--orange-soft); display: flex; align-items: center; justify-content: center;
    font-family: var(--serif); font-size: 26px; color: rgba(255,255,255,.32); }
  .service-name { flex: 1; display: flex; align-items: center; justify-content: center; text-align: center;
    font-family: var(--serif); font-size: 12px; letter-spacing: .6px; color: var(--white); line-height: 1.25; padding: 0 8px; }
  .service-name.cyan { background: var(--cyan); }
  .service-name.orange { background: var(--orange); }
</style>
</head>
<body>

  <section class="page cover">
    <header class="cover-head">
      <div class="brand"><span class="brand-mark"></span><span class="brand-name">Northvale inc.</span></div>
      <div class="brand-tagline">REAL ESTATE TECHNOLOGY CONSULTING</div>
    </header>
    <div class="cover-rule"></div>
    <div class="cover-photo" role="img" aria-label="Photo of a consultant and a mature couple looking at a small model house"></div>
    <div class="cover-band"><span class="cover-url">www.northvaleconsulting.com</span></div>
  </section>

  <div class="spread">
    <section class="page page-left">
      <div class="intro-panel">
        <h2 class="intro-title">CAPABILITY</h2>
        <p class="intro-text">Years of hands-on experience with property software, reliability and care. Clear, practical advice fitted to your needs, with help on everything from 'how to' questions to complex projects.</p>
      </div>
      <div class="photo-building" role="img" aria-label="Photo of business people talking in front of a modern white building"></div>
      <div class="photo-family" role="img" aria-label="Photo of a happy family playing outdoors under a bright sky"></div>
      <div class="ask-panel">
        <h2 class="ask-title">ASK US ABOUT ...</h2>
        <ul class="ask-list">
          <li>Automating financial reporting in Gridsheet</li>
          <li>Document Automation</li>
          <li>Enhancing your business processes with technology</li>
          <li>Optimizing your Ledgerly or Propvault system</li>
          <li>Help desk support for your system's customizations</li>
          <li>"Tune-up" trainings for employees</li>
        </ul>
      </div>
    </section>

    <section class="page page-right">
      <h1 class="services-title">OUR SERVICES</h1>
      <div class="services">
        <div class="service-row"><div class="service-number">1</div><div class="service-name cyan">PROCESS IMPROVEMENT</div></div>
        <div class="service-row"><div class="service-name orange">SYSTEM IMPLEMENTATION</div><div class="service-number">2</div></div>
        <div class="service-row"><div class="service-number">3</div><div class="service-name cyan">DATA CONVERSION</div></div>
        <div class="service-row"><div class="service-name orange">CUSTOMIZATION</div><div class="service-number">4</div></div>
        <div class="service-row"><div class="service-number">5</div><div class="service-name cyan">HELP DESK SUPPORT</div></div>
        <div class="service-row"><div class="service-name orange">TRAINING</div><div class="service-number">6</div></div>
        <div class="service-row"><div class="service-number">7</div><div class="service-name cyan">GRIDSHEET ANALYTICS</div></div>
        <div class="service-row tall"><div class="service-name orange">DASHBOARDS/BUSINESS<br>INTELLIGENCE</div><div class="service-number">8</div></div>
      </div>
    </section>
  </div>

</body>
</html>
```